Peter + Rob's 30th Birthday FB event cover photo

We're after a Facebook even cover photo for our 30th B'day. We live in Sydney
Peter + Rob's 30th Birthday

Venue (these details can be used in the graphic):
Quiet Heron
the basement of
The Marlow Hotel
42 Brackley St Fernhill
2 August 8pm-3am

The Marlow logo: http://www.themarlowhotelqz.com
Quiet Heron logo: http://quietheronpurrqz.com.au
The horizontal FaceBook cover photo for events has specific dimensions
As ideas I kind of like the styling of the dj poster (file attached) as a rough guide but not essential (i.e. no need to stick to that format/colours/dark shades) and Also the poster Pixel Harbour's Bruno did for Lumen Run
Thanks!

```html
<!DOCTYPE html>
<html lang="en">
<head>
<meta charset="utf-8">
<title>Peter + Rob's 30th Birthday</title>
<link rel="stylesheet" href="https://fonts.googleapis.com/css2?family=Bungee&family=Permanent+Marker&family=Teko:wght@400;500&family=Quicksand:wght@700&display=swap">
<style>
  :root {
    --teal-light: #8fd8c8;
    --teal: #4fbfa9;
    --teal-deep: #1f8f93;
    --navy: #2a3a78;
    --indigo: #35285f;
    --violet: #4b3a86;
    --pink: #d6308f;
    --pink-soft: #d36aa6;
    --sky: #39a8e0;
    --white: #ffffff;
  }
  html, body {
    margin: 0;
    padding: 0;
    overflow: hidden;
    background: var(--indigo);
  }
  .cover {
    position: relative;
    width: 1200px;
    height: 442px;
    overflow: hidden;
    background: linear-gradient(180deg, var(--teal-deep) 0%, #2c6b8f 30%, var(--navy) 60%, var(--indigo) 100%);
  }
  .cover-shapes {
    position: absolute;
    inset: 0;
  }
  .headline {
    position: absolute;
    left: 62px;
    top: 38px;
    margin: 0;
    font-family: "Bungee", sans-serif;
    font-weight: 400;
    font-size: 84px;
    line-height: 1;
    letter-spacing: 2px;
    color: var(--violet);
    text-shadow: -4px -3px 0 var(--white);
    white-space: nowrap;
  }
  .headline .plus {
    font-size: 54px;
    color: var(--white);
    text-shadow: none;
    vertical-align: 14px;
  }
  .age {
    position: absolute;
    left: 92px;
    top: 176px;
    font-family: "Quicksand", sans-serif;
    font-weight: 700;
    font-size: 84px;
    line-height: 1;
    color: var(--white);
    letter-spacing: -1px;
  }
  .age .suffix {
    font-size: 46px;
  }
  .occasion {
    position: absolute;
    left: 372px;
    top: 168px;
    font-family: "Permanent Marker", cursive;
    font-size: 88px;
    line-height: 1;
    color: var(--teal);
    letter-spacing: 8px;
    transform: skewX(-12deg);
  }
  .venue {
    position: absolute;
    left: 580px;
    top: 262px;
    width: 362px;
    font-family: "Teko", sans-serif;
    font-weight: 500;
    font-size: 36px;
    line-height: 0.9;
    text-transform: uppercase;
  }
  .venue-row {
    display: flex;
  }
  .venue-row + .venue-row {
    border-top: 3px solid var(--sky);
    margin-top: 4px;
    padding-top: 6px;
  }
  .venue-cell {
    padding-right: 9px;
    margin-right: 9px;
    border-right: 3px solid var(--sky);
  }
  .venue-cell:last-child {
    border-right: 0;
    padding-right: 0;
    margin-right: 0;
  }
  .is-white { color: var(--white); }
  .is-pink { color: var(--pink); }
  .partners {
    position: absolute;
    right: 28px;
    bottom: 24px;
    width: 140px;
    text-align: center;
    font-family: "Teko", sans-serif;
    font-weight: 500;
    font-size: 28px;
    line-height: 0.95;
    color: var(--white);
    text-transform: uppercase;
  }
  .partner + .partner {
    margin-top: 6px;
  }
</style>
</head>
<body>
<main class="cover">
  <svg class="cover-shapes" width="1200" height="442" viewBox="0 0 1200 442" aria-hidden="true">
    <defs>
      <linearGradient id="bowl-fill" x1="0" y1="0" x2="0" y2="1">
        <stop offset="0" stop-color="#d6308f"/>
        <stop offset="0.45" stop-color="#c3629f"/>
        <stop offset="1" stop-color="#8fd8c8"/>
      </linearGradient>
    </defs>
    <!-- large soft disc right -->
    <circle class="disc-large" cx="1065" cy="175" r="120" fill="#b7bfd8" opacity="0.45"/>
    <circle class="disc-corner" cx="1150" cy="420" r="200" fill="#6a5aa0" opacity="0.55"/>
    <!-- heading ribbon -->
    <polygon class="title-band" points="0,26 985,26 1065,150 0,150" fill="#8fd8c8"/>
    <!-- angular accents -->
    <polygon class="shard" points="1005,215 1200,150 1200,175" fill="#5bb9ae" opacity="0.75"/>
    <polygon class="shard" points="1110,240 1200,210 1200,290" fill="#5aa8b0" opacity="0.6"/>
    <polygon class="shard" points="370,282 245,392 300,330" fill="#3ab0a8" opacity="0.7"/>
    <polygon class="shard" points="220,298 470,250 470,262" fill="#3ab0a8" opacity="0.6"/>
    <polygon class="shard" points="505,268 560,250 520,300" fill="#6a8ab8" opacity="0.5"/>
    <polygon class="shard" points="15,305 120,340 40,345" fill="#3ab0a8" opacity="0.6"/>
    <!-- half bowl behind the age -->
    <path class="age-bowl" d="M55,170 L380,170 A162,162 0 0 1 55,170 Z" fill="url(#bowl-fill)"/>
    <!-- bubbles -->
    <g class="bubbles" fill="#d36aa6" opacity="0.85">
      <circle cx="58" cy="305" r="20"/>
      <circle cx="95" cy="295" r="7"/>
      <circle cx="100" cy="350" r="32"/>
      <circle cx="32" cy="350" r="7"/>
      <circle cx="196" cy="348" r="12"/>
      <circle cx="235" cy="310" r="32"/>
      <circle cx="270" cy="365" r="20"/>
      <circle cx="320" cy="345" r="8"/>
      <circle cx="395" cy="335" r="10"/>
      <circle cx="455" cy="310" r="10"/>
      <circle cx="465" cy="358" r="37"/>
      <circle cx="510" cy="400" r="11"/>
    </g>
  </svg>

  <h1 class="headline">PETER <span class="plus">+</span> ROB'S</h1>
  <div class="age">30<span class="suffix">th</span></div>
  <div class="occasion">BIRTHDAY</div>

  <section class="venue">
    <div class="venue-row">
      <div class="venue-cell is-white">Quiet<br>Heron</div>
      <div class="venue-cell is-pink">The basement of<br>The Marlow Hotel</div>
    </div>
    <div class="venue-row">
      <div class="venue-cell is-pink">42 Brackley<br>St Fernhill</div>
      <div class="venue-cell is-white">2 August<br>8PM–3AM</div>
    </div>
  </section>

  <div class="partners">
    <div class="partner">The Marlow</div>
    <div class="partner">Quiet Heron</div>
  </div>
</main>
</body>
</html>
```